verdant terraces simple classy business card design

my name is owen harlow and I run a gardening business aimed at high class verdant terraces. the business name is verdant terraces and our logo was designed on pixel forum .My clientel are anything from residential homes to businesses. I take pride in my work and know that I offer a service like no other in my area.
The business card will be used to represent my business and I want it to be not only rememberable, but simplistic and modern. Eye catching too. Of course I would like it relatable to gardening and appealing to the correct clientel - those being garden enthusiasts, prestigious homes and businesses that are after top of the line gardening services like no other on the market.
I am not a typical lawn mowing business so I don't want a typical card design that represents that. The gardens I work with are generally million dollar properties with owners who are very garden proud looking for upkeep and guidance from me along with sometimes whole new garden designs. I want the business cards to show to my clients that I take pride, as they do, in their garden. And I want them to know from my card that I am a professional, qualified horticulturist offering them a top of the line service for life. I want them to refer my business on. I want them to look at my business card and see class and professionalism in a modern unique bold way.
The card should be simple with the possibility of the logo on the front being embossed/debossed and my details on the back the card should have a organic garden feel it's very important to me that it is absolutely perfect
I am also very open to ideas and suggestions so look forward to seeing the designs. the business logo has been supplied with this project and I want the card to be double sided

Contact info is
Owen Harlow - Managing Director / Horticulturist
Phone : 0481 526 704
Email: owenharlow@verdantterraces.com.au

Target Market(s)

high class gardens residential and commercial

Industry/Entity Type

Gardener

Contact Information for Business Card

Contact info is
Phone : 0481 526 704

PLEASE MAKE CARD DOUBLE SIDED

Requirements
Must have
• organic simple classy modern feel
• must flow with the current logo that has been supplied with this project
• Double sided
• Must explain in a simple way that I deal with high end gardens and I'm a qualified horticulturist
Nice to have
• embossed debossed logo
Should not have
• shouldn't be to busy or cheap looking

```html
<!DOCTYPE html>
<html lang="en">
<head>
<meta charset="utf-8">
<title>Verdant Terraces – Business Card</title>
<link href="https://fonts.googleapis.com/css2?family=Cinzel:wght@400&family=Arvo:wght@400;700&display=swap" rel="stylesheet">
<style>
  :root {
    --backdrop: #e4e2de;
    --kraft: #a88f72;
    --kraft-light: #ad9478;
    --kraft-shade: #98805f;
    --ink: #141210;
  }
  html, body {
    margin: 0;
    padding: 0;
    width: 1200px;
    height: 1000px;
    overflow: hidden;
    background: var(--backdrop);
  }
  .defs { position: absolute; width: 0; height: 0; }
  .canvas {
    position: relative;
    width: 1200px;
    height: 1000px;
  }
  .card {
    position: absolute;
    left: 220px;
    width: 760px;
    height: 433px;
    border-radius: 24px;
    background: radial-gradient(ellipse at 50% 40%, var(--kraft-light) 0%, var(--kraft) 55%, var(--kraft-shade) 100%);
    overflow: hidden;
    color: var(--ink);
  }
  .card--front { top: 50px; }
  .card--back { top: 525px; }

  .paper-grain {
    position: absolute;
    inset: 0;
    width: 100%;
    height: 100%;
  }

  .brand-mark {
    position: absolute;
    left: 287px;
    top: 95px;
    width: 148px;
    height: 148px;
    border-radius: 50%;
    background: var(--ink);
  }
  .brand-name {
    position: absolute;
    left: 0;
    right: 0;
    text-align: center;
    font-family: "Cinzel", serif;
    font-weight: 400;
    color: var(--ink);
    margin: 0;
    line-height: 1;
  }
  .brand-name--primary {
    top: 240px;
    font-size: 66px;
    letter-spacing: 2px;
  }
  .brand-name--secondary {
    top: 309px;
    font-size: 38px;
    letter-spacing: 32px;
    padding-left: 32px;
  }

  .accent-disc {
    position: absolute;
    left: -110px;
    top: 0;
    width: 270px;
    height: 295px;
    border-radius: 50%;
    background: var(--ink);
  }

  .contact {
    position: absolute;
    left: 8px;
    right: 0;
    top: 0;
    bottom: 0;
    font-family: "Arvo", serif;
    line-height: 1;
  }
  .contact > * {
    position: absolute;
    left: 0;
    right: 0;
    margin: 0;
    text-align: center;
  }
  .contact__name {
    top: 148px;
    font-weight: 700;
    font-size: 21px;
    letter-spacing: 1.5px;
  }
  .contact__role {
    top: 178px;
    font-size: 20px;
  }
  .contact__rule {
    top: 216px;
    left: 352px;
    right: auto;
    width: 62px;
    height: 0;
    border: none;
    border-top: 1.5px solid var(--ink);
  }
  .contact__line { font-size: 20px; }
  .contact__line--phone { top: 236px; }
  .contact__line--email { top: 265px; }
  .contact__line--web { top: 294px; }
</style>
</head>
<body>
<svg class="defs" aria-hidden="true" focusable="false">
  <filter id="kraft-grain" x="0" y="0" width="100%" height="100%">
    <feTurbulence type="fractalNoise" baseFrequency="0.85" numOctaves="2" seed="7" result="fine"/>
    <feColorMatrix in="fine" type="matrix"
      values="0 0 0 0 0.25
              0 0 0 0 0.19
              0 0 0 0 0.12
              0 0 0 -2.2 1.35" result="fineSpeck"/>
    <feTurbulence type="fractalNoise" baseFrequency="0.04" numOctaves="3" seed="3" result="cloud"/>
    <feColorMatrix in="cloud" type="matrix"
      values="0 0 0 0 0.32
              0 0 0 0 0.25
              0 0 0 0 0.16
              0 0 0 -1.1 0.7" result="mottle"/>
    <feTurbulence type="turbulence" baseFrequency="0.22" numOctaves="1" seed="11" result="fibre"/>
    <feColorMatrix in="fibre" type="matrix"
      values="0 0 0 0 0.85
              0 0 0 0 0.78
              0 0 0 0 0.66
              0 0 0 -6 2.3" result="lightFleck"/>
    <feMerge>
      <feMergeNode in="mottle"/>
      <feMergeNode in="fineSpeck"/>
      <feMergeNode in="lightFleck"/>
    </feMerge>
  </filter>
</svg>

<main class="canvas">
  <section class="card card--front" aria-label="Card front">
    <svg class="paper-grain" aria-hidden="true"><rect width="100%" height="100%" filter="url(#kraft-grain)" opacity="0.35"/></svg>
    <div class="brand-mark" aria-hidden="true"></div>
    <h1 class="brand-name brand-name--primary">VERDANT</h1>
    <p class="brand-name brand-name--secondary">TERRACES</p>
  </section>

  <section class="card card--back" aria-label="Card back">
    <svg class="paper-grain" aria-hidden="true"><rect width="100%" height="100%" filter="url(#kraft-grain)" opacity="0.35"/></svg>
    <div class="accent-disc" role="img" aria-label="Large dark tree silhouette cropped at the card edge"></div>
    <div class="contact">
      <p class="contact__name">OWEN HARLOW</p>
      <p class="contact__role">Managing Director / Horticulturist</p>
      <hr class="contact__rule">
      <p class="contact__line contact__line--phone">0481 526 704</p>
      <p class="contact__line contact__line--email">owenharlow@verdantterraces.com.au</p>
      <p class="contact__line contact__line--web">www.verdantterraces.com.au</p>
    </div>
  </section>
</main>
</body>
</html>
```